New Business Card Design Project

Want a simple but attention grabbing business card. Back Side having mainly our logo and basic info-the front side a typical business card.

Contact Information for Business Card

Hearth & Basin Works
218 NW Larkfield Rd. Suite 207
Ankeny, Iowa 50021

phone- 515.284.7093

website is -hbwplains.com

```html
<!DOCTYPE html>
<html lang="en">
<head>
<meta charset="utf-8">
<title>Hearth &amp; Basin Works – Business Card</title>
<link rel="stylesheet" href="https://fonts.googleapis.com/css2?family=Josefin+Sans:wght@300;400;600;700&display=swap">
<style>
  :root {
    --page-bg: #e8e9ec;
    --card-white: #f1f1f3;
    --brand-orange: #e0531f;
    --brand-blue: #1f69b0;
    --text-grey: #6e6e70;
    --white: #ffffff;
  }
  * { box-sizing: border-box; margin: 0; padding: 0; }
  html, body {
    width: 1200px; height: 1200px; overflow: hidden;
    background: var(--page-bg);
    font-family: "Josefin Sans", sans-serif;
  }
  .card {
    position: absolute;
    left: 227px;
    width: 746px;
    height: 426px;
    border-radius: 28px;
    overflow: hidden;
  }
  .card--front { top: 135px; background: var(--card-white); }
  .card--back  { top: 639px; background: var(--brand-blue); display: flex; align-items: center; justify-content: center; }

  .side-band { position: absolute; left: 0; top: 0; width: 40px; height: 100%; background: var(--brand-blue); }
  .side-band__top { position: absolute; left: 0; top: 0; width: 40px; height: 72px; background: var(--brand-orange); }

  .brand-name {
    position: absolute; left: 73px; top: 122px;
    font-size: 33px; font-weight: 700; color: var(--brand-orange);
    letter-spacing: 0.5px; text-transform: uppercase;
  }
  .person { position: absolute; left: 73px; top: 231px; }
  .person__name { font-size: 27px; font-weight: 600; letter-spacing: 0.5px; text-transform: uppercase; }
  .person__first { color: var(--brand-orange); }
  .person__last { color: var(--brand-blue); }
  .person__title { font-size: 19px; font-weight: 300; color: var(--text-grey); margin-top: 4px; }
  .rule { position: absolute; left: 254px; right: 0; top: 275px; height: 2px; background: var(--brand-blue); }

  .contacts { position: absolute; left: 73px; top: 316px; list-style: none; }
  .contacts li { display: flex; align-items: center; height: 25px; font-size: 19px; font-weight: 300; color: var(--text-grey); }
  .contacts svg { width: 18px; height: 18px; margin-right: 12px; flex: none; }

  .address {
    position: absolute; right: 39px; top: 338px; text-align: right;
    font-size: 19px; font-weight: 300; color: var(--text-grey); line-height: 25px; font-style: normal;
  }

  .back-name {
    font-size: 40px; font-weight: 700; color: var(--white);
    letter-spacing: 0.5px; text-transform: uppercase;
  }
</style>
</head>
<body>
  <section class="card card--front">
    <div class="side-band"><div class="side-band__top"></div></div>
    <div class="brand-name">Hearth &amp; Basin Works</div>

    <div class="person">
      <div class="person__name"><span class="person__first">Dale</span> <span class="person__last">Hartwell</span></div>
      <div class="person__title">Managing Director</div>
    </div>
    <div class="rule"></div>

    <ul class="contacts">
      <li>
        <svg viewBox="0 0 18 18" aria-hidden="true"><circle cx="9" cy="9" r="9" fill="var(--brand-orange)"/><path d="M5 7.5c0-1.5 8-1.5 8 0v1h-2v-1h-4v1H5z M6.5 9h5l1 4h-7z" fill="#fff"/></svg>
        (515) 284-7093
      </li>
      <li>
        <svg viewBox="0 0 18 18" aria-hidden="true"><circle cx="9" cy="9" r="9" fill="var(--brand-orange)"/><rect x="4.5" y="5.8" width="9" height="6.4" fill="none" stroke="#fff" stroke-width="1.2"/><path d="M4.5 6l4.5 3.6L13.5 6" fill="none" stroke="#fff" stroke-width="1.2"/></svg>
        info@hbwplains.com
      </li>
      <li>
        <svg viewBox="0 0 18 18" aria-hidden="true"><circle cx="9" cy="9" r="9" fill="var(--brand-orange)"/><circle cx="9" cy="9" r="5" fill="none" stroke="#fff" stroke-width="1.2"/><path d="M4 9h10M9 4c-2.5 3-2.5 7 0 10M9 4c2.5 3 2.5 7 0 10" fill="none" stroke="#fff" stroke-width="1"/></svg>
        www.hbwplains.com
      </li>
    </ul>

    <address class="address">
      218 Northwest Larkfield Road<br>
      Suite 207,&nbsp; Ankeny, IA 50021
    </address>
  </section>

  <section class="card card--back">
    <div class="back-name">Hearth &amp; Basin Works</div>
  </section>
</body>
</html>
```